uDRAV AirCargo Trailer Wrap

Project: Full exterior livery design for our air cargo road transport trailer., Trailer type: Pravik Mega Trailer
Base color: White (must remain dominant) About Us UDRAV specializes in air freight road transportation. We transport air cargo:
Airport β†’ Logistics hubs
Manufacturers β†’ Airport
We are a last-mile logistics partner in the air cargo industry. A clean, modern, and highly recognizable trailer design that instantly communicates: ✈ Air Cargo πŸš› Road Transport 🌍 International Logistics πŸ”· UDRAV brand The design must be minimal but strong.
Professional, premium, and visible from distance.

Design Goals
Clear and bold UDRAV logo placement
Strong highway visibility
Aviation-inspired visual elements (subtle, not clichΓ©)
Modern, industrial typography
Clean composition – no clutter
Avoid: overly busy graphics, cartoon airplanes, generic stock icons.
Deliverables
Left side view
Right side view
Rear view

We are looking for a design that makes people immediately think:
β€œAir cargo. Professional. Reliable.”

Target Market(s)

Forwarding

Industry/Entity Type

Transportation

Requirements
Must have
• "LINEHAUL" tag "UDRAV logo+ LINEHAUL"
Nice to have
Should not have
• Air cargo/Air freight/Express is boring..

```html
<!DOCTYPE html>
<html lang="en">
<head>
<meta charset="utf-8">
<title>uDRAV Linehaul Trailer Livery</title>
<link rel="stylesheet" href="https://fonts.googleapis.com/css2?family=Poppins:wght@700&family=Barlow+Semi+Condensed:wght@600&display=swap">
<style>
  :root {
    --canvas: #eceef1;
    --panel: #ffffff;
    --panel-edge: #c9ccd1;
    --panel-line: #dfe2e6;
    --ink: #1b1b1d;
    --brand-red: #c8293e;
    --plane-dark: #1f1f22;
    --plane-mid: #3a3a3f;
  }
  * { box-sizing: border-box; margin: 0; padding: 0; }
  html, body { width: 1200px; height: 2229px; overflow: hidden; }
  body { background: var(--canvas); position: relative; font-family: "Poppins", sans-serif; }

  .view { position: absolute; left: 0; width: 1200px; }
  .view--right-rear { top: 0; height: 870px; }
  .view--side { top: 870px; height: 520px; }
  .view--left-front { top: 1390px; height: 839px; }

  .panel {
    position: absolute;
    background: var(--panel);
    border: 2px solid var(--panel-edge);
  }
  .panel::after {
    content: "";
    position: absolute;
    left: 0; right: 0; bottom: 18px;
    height: 4px;
    background: var(--panel-line);
  }

  .rear-doors .door-frame {
    position: absolute; inset: 22px 18px 40px 18px;
    border: 4px solid var(--brand-red);
  }
  .rear-doors .door-split {
    position: absolute; top: 22px; bottom: 40px; left: 50%;
    width: 4px; margin-left: -2px; background: var(--panel-edge);
  }

  .logo { position: absolute; display: flex; flex-direction: column; align-items: center; z-index: 1; }
  .logo-lockup { display: flex; align-items: center; white-space: nowrap; }
  .logo-mark {
    border-radius: 50%;
    background: var(--brand-red);
    flex: none;
  }
  .logo-name {
    color: var(--ink);
    font-weight: 700;
    letter-spacing: 0.01em;
    line-height: 1;
  }
  .logo-tag {
    font-family: "Barlow Semi Condensed", sans-serif;
    font-weight: 600;
    color: var(--brand-red);
    line-height: 1;
    white-space: nowrap;
  }

  .plane-art {
    position: absolute;
    border-radius: 40% 60% 45% 55% / 50% 40% 60% 50%;
    background: linear-gradient(135deg, var(--plane-mid) 0%, var(--plane-dark) 55%, var(--brand-red) 56%, var(--plane-dark) 60%);
    opacity: 0.92;
  }
</style>
</head>
<body>

<section class="view view--right-rear" aria-label="Right side and rear view">
  <div class="panel side-panel" style="left:30px; top:140px; width:790px; height:520px;">
    <div class="logo" style="left:40px; top:200px;">
      <div class="logo-lockup" style="gap:10px;">
        <span class="logo-mark" style="width:20px; height:20px;"></span>
        <span class="logo-name" style="font-size:62px;">UDRAV</span>
      </div>
      <span class="logo-tag" style="font-size:22px; letter-spacing:0.2em; margin-top:10px;">LINEHAUL</span>
    </div>
    <div class="plane-art" role="img" aria-label="Illustration of a black jet airliner with a red stripe climbing upward" style="left:340px; top:30px; width:400px; height:440px;"></div>
  </div>
  <div class="panel rear-doors" style="left:850px; top:60px; width:320px; height:690px;">
    <span class="door-frame"></span>
    <span class="door-split"></span>
    <div class="logo" style="left:0; right:0; top:300px;">
      <div class="logo-lockup" style="gap:8px;">
        <span class="logo-mark" style="width:16px; height:16px;"></span>
        <span class="logo-name" style="font-size:52px;">UDRAV</span>
      </div>
      <span class="logo-tag" style="font-size:20px; letter-spacing:0.2em; margin-top:10px;">LINEHAUL</span>
    </div>
  </div>
</section>

<section class="view view--side" aria-label="Side view">
  <div class="panel side-panel" style="left:18px; top:100px; width:1164px; height:260px;">
    <div class="logo" style="left:130px; top:45px;">
      <div class="logo-lockup" style="gap:14px;">
        <span class="logo-mark" style="width:28px; height:28px;"></span>
        <span class="logo-name" style="font-size:100px;">UDRAV</span>
      </div>
      <span class="logo-tag" style="font-size:24px; letter-spacing:0.32em; margin-top:8px;">LINEHAUL</span>
    </div>
    <div class="plane-art" role="img" aria-label="Illustration of a black jet airliner with a red stripe climbing to the right" style="left:580px; top:28px; width:490px; height:200px;"></div>
  </div>
</section>

<section class="view view--left-front" aria-label="Front and left side view">
  <div class="panel front-panel" style="left:18px; top:150px; width:200px; height:520px;">
    <div class="logo" style="left:0; right:0; top:200px;">
      <div class="logo-lockup" style="gap:6px;">
        <span class="logo-mark" style="width:12px; height:12px;"></span>
        <span class="logo-name" style="font-size:36px;">UDRAV</span>
      </div>
      <span class="logo-tag" style="font-size:15px; letter-spacing:0.18em; margin-top:8px;">LINEHAUL</span>
    </div>
  </div>
  <div class="panel side-panel" style="left:238px; top:150px; width:944px; height:520px;">
    <div class="logo" style="left:70px; top:160px;">
      <div class="logo-lockup" style="gap:16px;">
        <span class="logo-mark" style="width:34px; height:34px;"></span>
        <span class="logo-name" style="font-size:112px;">UDRAV</span>
      </div>
      <span class="logo-tag" style="font-size:34px; letter-spacing:0.2em; margin-top:22px;">LINEHAUL</span>
    </div>
    <div class="plane-art" role="img" aria-label="Illustration of a black jet airliner with a red stripe climbing upward" style="left:580px; top:120px; width:320px; height:260px;"></div>
  </div>
</section>

</body>
</html>
```